Halvorsen Partners Business Card

Halvorsen Partners Civil Construction
Marcus Halvorsen
CEO
727-518-6094
Marcus@HalvorsenSiteworks.example
www.HalvorsenSiteworks.example
Site Development
Utility Construction
Excavation
40876 County Lane 19
Land O' Lakes, FL 34638

Target Market(s)

Construction and government

Industry/Entity Type

Business

Contact Information for Business Card

I want an unique design that make a statement

Number of Pages Required

1 page

Font styles to use

Colors

Designer to choose colors to be used in the design.

Requirements
Must have
• unique design, feel free to modify or change the color of my logo.
Nice to have
• extra design features like spot UV, foil accents, color edges, unique paper, or any thing that would make my card pop.
• I like the feel of the image that I attached

```html
<!DOCTYPE html>
<html lang="en">
<head>
<meta charset="utf-8">
<title>Halvorsen Partners Business Card</title>
<link rel="stylesheet" href="https://fonts.googleapis.com/css2?family=Stint+Ultra+Condensed&display=swap">
<style>
  :root {
    --page: #ffffff;
    --front-sky-top: #b9c0bf;
    --front-sky-mid: #c9cfcd;
    --front-ground: #8a8d8c;
    --front-ink: #3e4545;
    --back-sky-top: #5d6161;
    --back-sky-mid: #b9bebe;
    --back-ground: #0d0d0d;
    --band: #111111;
    --band-wing: #262828;
    --band-core: #070808;
    --frame: #1a1a1a;
    --mark: #3a49c9;
    --name-ink: #8d9ae8;
    --sub-ink: #b8bcbc;
  }
  * { margin: 0; padding: 0; box-sizing: border-box; }
  html, body { width: 1200px; height: 1040px; overflow: hidden; background: var(--page); }
  body { position: relative; font-family: "Stint Ultra Condensed", "Arial Narrow", serif; }

  .card { position: absolute; left: 274px; width: 623px; height: 390px; overflow: hidden; }
  .card--front { top: 54px; }
  .card--back { top: 512px; }

  .card__photo { position: absolute; inset: 0; }
  .card--front .card__photo {
    background: linear-gradient(180deg, var(--front-sky-top) 0%, var(--front-sky-mid) 60%, #c3c8c6 88%, var(--front-ground) 94%, var(--front-ground) 100%);
  }
  .card--back .card__photo {
    background: linear-gradient(180deg, var(--back-sky-top) 0%, #8e9393 18%, var(--back-sky-mid) 45%, #d4d8d8 80%, #5a5d5d 92%, var(--back-ground) 96%);
  }

  .line { position: absolute; left: 132px; color: var(--front-ink); white-space: nowrap; line-height: 30px; font-size: 26px; }
  .front__company { top: 24px; font-size: 36px; letter-spacing: 0.5px; }
  .front__name { top: 77px; }
  .front__title {
    position: absolute; right: 497px; top: 58px; line-height: 70px; font-size: 78px;
    color: var(--front-ink); white-space: nowrap;
  }
  .front__contact-label {
    position: absolute; left: 52px; top: 284px; width: 120px; height: 20px; line-height: 20px;
    font-size: 20px; color: var(--front-ink); text-align: center; white-space: nowrap;
    transform: rotate(-90deg); transform-origin: center;
  }
  .front__bracket { position: absolute; left: 0; top: 0; }

  .back__svg { position: absolute; inset: 0; }
  .back__brand {
    position: absolute; left: 232px; top: 134px; line-height: 32px; font-size: 32px; color: var(--name-ink);
    text-transform: uppercase; letter-spacing: 1px; white-space: nowrap;
  }
  .back__sub {
    position: absolute; left: 233px; top: 166px; line-height: 16px; font-size: 16px; color: var(--sub-ink);
    text-transform: uppercase; letter-spacing: 5px; white-space: nowrap;
  }
</style>
</head>
<body>

  <section class="card card--front" aria-label="Business card front">
    <div class="card__photo" role="img" aria-label="Faded photo of a cloudy sky over a site with an excavator loading a dump truck"></div>
    <div class="line front__company">Halvorsen Partners Civil Construction</div>
    <div class="front__title">CEO</div>
    <div class="line front__name">Marcus Halvorsen</div>
    <div class="line" style="top:125px">Site Development</div>
    <div class="line" style="top:154px">Utility Construction</div>
    <div class="line" style="top:184px">Excavation</div>
    <svg class="front__bracket" width="623" height="390" aria-hidden="true">
      <polyline points="134,219 127,219 127,368 171,368" fill="none" stroke="var(--front-ink)" stroke-width="1"/>
    </svg>
    <div class="front__contact-label">contact info</div>
    <div class="line" style="top:219px">727-518-6094</div>
    <div class="line" style="top:249px">Marcus@HalvorsenSiteworks.example</div>
    <div class="line" style="top:279px">www.HalvorsenSiteworks.example</div>
    <div class="line" style="top:309px">40876 County Lane 19</div>
    <div class="line" style="top:339px">Land O' Lakes, FL 34638</div>
  </section>

  <section class="card card--back" aria-label="Business card back">
    <div class="card__photo" role="img" aria-label="Photo of a stormy grey sky with silhouettes of a bulldozer, excavator and dump truck"></div>
    <svg class="back__svg" width="623" height="390" aria-hidden="true">
      <rect x="8" y="9" width="604" height="372" fill="none" stroke="var(--frame)" stroke-width="2"/>
      <rect x="0" y="126" width="623" height="74" fill="var(--band)"/>
      <polygon points="74,126 127,106 127,220 74,200" fill="var(--band-wing)"/>
      <polygon points="548,126 495,106 495,220 548,200" fill="var(--band-wing)"/>
      <rect x="127" y="106" width="368" height="114" fill="var(--band-core)"/>
      <rect x="158" y="136" width="50" height="52" fill="none" stroke="var(--mark)" stroke-width="4"/>
      <line x1="223" y1="128" x2="223" y2="198" stroke="#6c7070" stroke-width="2"/>
    </svg>
    <div class="back__brand">Halvorsen Partners</div>
    <div class="back__sub">Civil Construction</div>
  </section>

</body>
</html>
```